Bright Ledger Advert Flyer for KOREMIViewpoints magazine

Bright Ledger need a 1 A4 Full Page color advertisement created for the upcoming issues featured in the printed magazine. https://www.koremiviewpoint.com/magazines/September2017/BigData/

Brightledger.com.au

Your trusted Data & Analytics Partner

Focused Data driven solutions & services provider
Proven experience and trusted technologies

Quorvante
VTL
Big Data
Cloud Architecture
Advanced Analytics

```html
<!DOCTYPE html>
<html lang="en">
<head>
<meta charset="utf-8">
<title>Bright Ledger – Full Page Advertisement</title>
<link href="https://fonts.googleapis.com/css2?family=Roboto+Condensed:wght@400;700&family=Roboto:wght@400;500;700&display=swap" rel="stylesheet">
<style>
  :root {
    --page-bg: #f2f2f2;
    --panel-top: #8f2a17;
    --panel-bottom: #c4441e;
    --text-light: #ffffff;
    --sky-top: #5f6f82;
    --sky-mid: #b96a4e;
    --sky-glow: #e3702c;
    --sky-low: #c0401c;
    --sky-bottom: #6e1a12;
  }
  * { box-sizing: border-box; margin: 0; padding: 0; }
  html, body {
    width: 1046px; height: 1200px; overflow: hidden;
    background: var(--page-bg);
  }
  .advert {
    position: absolute; left: 113px; top: 20px;
    width: 820px; height: 1160px;
    display: flex;
    box-shadow: 0 4px 14px rgba(0,0,0,0.25);
  }
  .advert__panel {
    position: relative;
    width: 432px; height: 100%;
    background: linear-gradient(180deg, var(--panel-top) 0%, #a8361a 45%, var(--panel-bottom) 100%);
    color: var(--text-light);
    font-family: "Roboto", sans-serif;
  }
  .advert__photo {
    flex: 1; height: 100%;
    background: linear-gradient(180deg, var(--sky-top) 0%, #7d7a86 22%, var(--sky-mid) 42%, var(--sky-glow) 58%, var(--sky-low) 76%, var(--sky-bottom) 100%);
  }
  .brand {
    position: absolute; left: 34px; top: 72px;
    display: flex; align-items: center; gap: 10px;
    font-family: "Roboto", sans-serif; font-weight: 500;
    font-size: 42px; line-height: 1; color: var(--text-light);
    letter-spacing: -0.5px;
  }
  .brand__mark {
    width: 14px; height: 14px; background: var(--text-light);
  }
  .headline {
    position: absolute; left: 36px; top: 220px;
    font-family: "Roboto Condensed", sans-serif;
    font-size: 72px; line-height: 74px; text-transform: uppercase;
  }
  .headline__light { display: block; font-weight: 400; }
  .headline__bold { display: block; font-weight: 700; }
  .summary {
    position: absolute; left: 36px; top: 672px; width: 352px;
    font-size: 17px; font-weight: 700; line-height: 23px;
  }
  .services {
    position: absolute; left: 36px; top: 762px;
    list-style: none;
  }
  .services__item {
    display: flex; align-items: center; gap: 12px;
    font-size: 19px; line-height: 32px;
  }
  .services__icon { width: 13px; height: 13px; }
  .contact {
    position: absolute; left: 36px; top: 1016px;
  }
  .contact__row {
    display: flex; align-items: center; gap: 8px;
  }
  .contact__icon { width: 13px; height: 13px; flex: none; }
  .contact__phone { font-size: 15px; line-height: 22px; }
  .contact__email { font-size: 11px; line-height: 20px; }
  .contact__web { font-size: 26px; font-weight: 500; line-height: 36px; }
  .contact__web .contact__icon { width: 15px; height: 15px; }
</style>
</head>
<body>
  <main class="advert">
    <section class="advert__panel">
      <div class="brand"><span class="brand__mark"></span>Bright Ledger</div>

      <h1 class="headline">
        <span class="headline__light">Your</span>
        <span class="headline__light">Trusted</span>
        <span class="headline__bold">Data &amp;</span>
        <span class="headline__bold">Analytics</span>
        <span class="headline__bold">Partner</span>
      </h1>

      <p class="summary">Focused Data driven solutions &amp; services provider Proven experience and trusted technologies</p>

      <ul class="services">
        <li class="services__item"><svg class="services__icon" viewBox="0 0 12 12"><path d="M2 2L10 10M10 2L2 10" stroke="#fff" stroke-width="2"/></svg>Quorvante</li>
        <li class="services__item"><svg class="services__icon" viewBox="0 0 12 12"><path d="M2 2L10 10M10 2L2 10" stroke="#fff" stroke-width="2"/></svg>VTL</li>
        <li class="services__item"><svg class="services__icon" viewBox="0 0 12 12"><path d="M2 2L10 10M10 2L2 10" stroke="#fff" stroke-width="2"/></svg>Big Data</li>
        <li class="services__item"><svg class="services__icon" viewBox="0 0 12 12"><path d="M2 2L10 10M10 2L2 10" stroke="#fff" stroke-width="2"/></svg>Cloud Architecture</li>
        <li class="services__item"><svg class="services__icon" viewBox="0 0 12 12"><path d="M2 2L10 10M10 2L2 10" stroke="#fff" stroke-width="2"/></svg>Advanced Analytics</li>
      </ul>

      <div class="contact">
        <div class="contact__row contact__phone">
          <svg class="contact__icon" viewBox="0 0 12 12"><path d="M3 1.5L5 3.5L4 5C4.8 6.6 5.6 7.4 7 8L8.5 7L10.5 9L9 10.8C5 10.5 1.5 7 1.2 3Z" fill="#fff"/></svg>
          <span>1300 BLEDGER (253 343)</span>
        </div>
        <div class="contact__row contact__email">
          <svg class="contact__icon" viewBox="0 0 12 12"><rect x="1" y="3" width="10" height="7" fill="#fff"/><path d="M1 3L6 7L11 3" stroke="#b33c1b" stroke-width="1" fill="none"/></svg>
          <span>enquiries@brightledger.com.au</span>
        </div>
        <div class="contact__row contact__web">
          <svg class="contact__icon" viewBox="0 0 12 12"><circle cx="6" cy="6" r="5" fill="none" stroke="#fff" stroke-width="1.2"/><ellipse cx="6" cy="6" rx="2.2" ry="5" fill="none" stroke="#fff" stroke-width="1"/><path d="M1 6H11" stroke="#fff" stroke-width="1"/></svg>
          <span>Brightledger.com.au</span>
        </div>
      </div>
    </section>

    <div class="advert__photo" role="img" aria-label="Photograph of two climbers in silhouette on a rock face, one reaching down to help the other, against a sunset sky fading from grey-blue to deep orange and red"></div>
  </main>
</body>
</html>
```